Business Card Design Project

Hi,
This is a simple contest. The logo for the back of the card is deigned. See attached files. The front of the card must have :

Directors Name: Dorian
Mob:
e-mail:
Postal Address:
Web Page Adress:

It may also add words: "Leaders in Construction Project Management Services"

Target Market(s)

Business & Home owners alike

Industry/Entity Type

Business

Requirements
Must have
• See details above and logo attached
Should not have
• Images other than logo

```html
<!DOCTYPE html>
<html lang="en">
<head>
<meta charset="utf-8">
<title>Keystone Build Partners – Business Card</title>
<link href="https://fonts.googleapis.com/css2?family=Tenor+Sans&display=swap" rel="stylesheet">
<style>
  :root {
    --backdrop: #2b2b2b;
    --paper: #ffffff;
    --sky-blue: #1a9ad6;
    --logo-blue: #2f8fd6;
    --ink-navy: #0e3e5e;
    --deep-blue-light: #1c86bb;
    --deep-blue-dark: #0a4a6e;
    --white: #ffffff;
  }
  * { margin: 0; padding: 0; box-sizing: border-box; }
  html, body {
    width: 1200px; height: 900px; overflow: hidden;
    background: var(--backdrop);
    font-family: "Tenor Sans", sans-serif;
  }
  .canvas { position: relative; width: 1200px; height: 900px; }

  .card {
    position: absolute;
    width: 640px; height: 360px;
    overflow: hidden;
  }

  /* Front: contact side */
  .card-front { left: 50px; top: 80px; background: var(--sky-blue); }
  .card-front .top-band {
    position: absolute; left: 0; top: 0; width: 100%; height: 140px;
    background: var(--paper);
  }
  .brand {
    position: absolute; display: flex; align-items: center; gap: 16px;
  }
  .brand-mark { flex: none; }
  .brand-name { line-height: 1; letter-spacing: 2px; }
  .card-front .brand { left: 130px; top: 40px; }
  .card-front .brand-mark { width: 56px; height: 56px; background: var(--logo-blue); }
  .card-front .brand-name { color: var(--logo-blue); font-size: 30px; }

  .person {
    position: absolute; left: 130px; top: 248px;
    color: var(--ink-navy); font-size: 19px; line-height: 1.1;
    text-transform: uppercase;
  }
  .contact {
    position: absolute; left: 300px; top: 178px;
    display: grid; grid-template-columns: auto auto; column-gap: 10px; row-gap: 4px;
    font-size: 17px; text-transform: uppercase;
  }
  .contact dt { color: var(--ink-navy); text-align: right; }
  .contact dd { color: var(--white); }

  /* Back: brand side */
  .card-back {
    left: 510px; top: 470px; width: 660px; height: 380px;
    background: radial-gradient(ellipse at 45% 35%, var(--deep-blue-light) 0%, var(--deep-blue-dark) 80%);
  }
  .card-back .brand { left: 90px; top: 130px; }
  .card-back .brand-mark { width: 80px; height: 80px; background: var(--white); }
  .card-back .brand-name { color: var(--white); font-size: 40px; }
  .tagline {
    position: absolute; left: 0; width: 100%; top: 290px;
    text-align: center; color: var(--white); font-size: 17px;
  }
</style>
</head>
<body>
<main class="canvas">
  <section class="card card-front">
    <div class="top-band">
      <div class="brand">
        <span class="brand-mark"></span>
        <span class="brand-name">KEYSTONE BUILD PARTNERS</span>
      </div>
    </div>
    <p class="person">Dorian<br>Director</p>
    <dl class="contact">
      <dt>Mobile :</dt><dd>555 014 2290</dd>
      <dt>Email :</dt><dd>Dorian@kbpmail.com</dd>
      <dt>Address :</dt><dd>Marlow Bay, NSW 2087</dd>
      <dt>Website :</dt><dd>www.kbp-build.com</dd>
    </dl>
  </section>

  <section class="card card-back">
    <div class="brand">
      <span class="brand-mark"></span>
      <span class="brand-name">KEYSTONE BUILD<br>PARTNERS</span>
    </div>
    <p class="tagline">"Leaders in Construction Project Management Services"</p>
  </section>
</main>
</body>
</html>
```